Wholesale Fashion Agent

Industry/Entity Type

Fashion

Contact Information for Business Card

I have attached the previous logo, we are wanting to re-vamp with black and white only. Sharp and more modern.

Mirela Stonecroft Agencies back of card
address (to be advised, as we are moving)

MS Agencies front of card, with Fashion Agent on the front

```html
<!DOCTYPE html>
<html lang="en">
<head>
<meta charset="utf-8">
<title>Mirela Stonecroft Agencies – Business Card</title>
<link href="https://fonts.googleapis.com/css2?family=Share+Tech+Mono&display=swap" rel="stylesheet">
<style>
  :root {
    --paper: #ffffff;
    --card: #0b0b0b;
    --card-edge: #1c1c1c;
    --ink: #f4d9d6;
    --reflection: #262626;
    --mark: #5a6365;
    --figure-top: #f6e6e4;
    --figure-bottom: #2a2a2a;
  }
  * { margin: 0; padding: 0; box-sizing: border-box; }
  html, body {
    width: 918px;
    height: 1200px;
    overflow: hidden;
    background: var(--paper);
  }
  .sheet {
    position: relative;
    width: 918px;
    height: 1200px;
  }
  .card {
    position: absolute;
    left: 0;
    width: 918px;
    background: var(--card);
    border: 3px solid var(--card-edge);
    overflow: hidden;
    font-family: "Share Tech Mono", "Courier New", monospace;
    text-transform: uppercase;
    color: var(--ink);
  }
  .card--front { top: 0; height: 564px; }
  .card--back { top: 631px; height: 569px; }

  .text-block {
    position: absolute;
    white-space: nowrap;
  }
  .text-block p { display: block; }

  /* Front */
  .address-block {
    left: 270px;
    font-size: 30px;
    letter-spacing: 8px;
  }
  .address-block .company {
    line-height: 40px;
    margin-bottom: 62px;
    letter-spacing: 6px;
  }
  .address-block .address-line { line-height: 51px; }

  .front-details { top: 33px; }
  .front-reflection {
    top: 282px;
    color: var(--reflection);
    transform-origin: 0 0;
    transform: translateY(191px) scaleY(-0.75);
  }

  .figure-art {
    position: absolute;
    left: 14px;
    top: 58px;
    width: 205px;
    height: 360px;
  }
  .brand-lockup {
    position: absolute;
    left: 18px;
    top: 432px;
    white-space: nowrap;
  }
  .brand-name {
    font-size: 26px;
    letter-spacing: 4px;
    line-height: 34px;
    color: var(--mark);
  }
  .brand-tagline {
    margin-top: 8px;
    font-size: 20px;
    letter-spacing: 5px;
    line-height: 26px;
    color: var(--ink);
  }

  /* Back */
  .contact-block {
    left: 33px;
    font-size: 30px;
    letter-spacing: 4.6px;
  }
  .contact-block p { line-height: 43px; }
  .contact-block .web-line { font-size: 24px; letter-spacing: 8px; }

  .contact-list { top: 76px; }
  .contact-reflection {
    top: 280px;
    color: var(--reflection);
    transform-origin: 0 0;
    transform: translateY(195px) scaleY(-0.89);
  }
</style>
</head>
<body>
<main class="sheet">

  <section class="card card--front" aria-label="Front of card">
    <svg class="figure-art" viewBox="0 0 205 360" role="img" aria-label="Line illustration of a woman in a long gown">
      <defs>
        <linearGradient id="figureTone" x1="0" y1="0" x2="0" y2="1">
          <stop offset="0" stop-color="var(--figure-top)" stop-opacity="0.35"/>
          <stop offset="1" stop-color="var(--figure-bottom)" stop-opacity="0.6"/>
        </linearGradient>
      </defs>
      <rect x="0" y="0" width="205" height="360" rx="10" fill="url(#figureTone)"/>
    </svg>

    <div class="brand-lockup">
      <p class="brand-name">MS Agencies</p>
      <p class="brand-tagline">Fashion Agent</p>
    </div>

    <div class="text-block address-block front-details">
      <p class="company">Mirela Stonecroft agencies</p>
      <p class="address-line">unit 4/12 harlow street</p>
      <p class="address-line">west endley qld 4190</p>
      <p class="address-line">australia</p>
    </div>

    <div class="text-block address-block front-reflection" aria-hidden="true">
      <p class="company">Mirela Stonecroft agencies</p>
      <p class="address-line">unit 4/12 harlow street</p>
      <p class="address-line">west endley qld 4190</p>
      <p class="address-line">australia</p>
    </div>
  </section>

  <section class="card card--back" aria-label="Back of card">
    <div class="text-block contact-block contact-list">
      <p>P:07-3900 1274</p>
      <p>F:07-3900 1288</p>
      <p>M:0400 512 736</p>
      <p class="web-line">E: mirela@msagencies.com.au</p>
      <p class="web-line">W: www.msagencies.com.au</p>
    </div>

    <div class="text-block contact-block contact-reflection" aria-hidden="true">
      <p>P:07-3900 1274</p>
      <p>F:07-3900 1288</p>
      <p>M:0400 512 736</p>
      <p class="web-line">E: mirela@msagencies.com.au</p>
      <p class="web-line">W: www.msagencies.com.au</p>
    </div>
  </section>

</main>
</body>
</html>
```